I need email signatures for my admin staff members
info:
Darina Qubrosi
Support Coordinator
Unit 4, 517 Wattlebrook Lane, Kemberly NSW 2893
Tel: 02 84427193 Mob: 0427596314
email: darina.qu@mivrotelhaven.com
www.mivrotelhaven.com

Target Market(s)

community services industry

Industry/Entity Type

Community Service

Requirements
Must have
• Specialist Provider of Multicultural Support Services
Nice to have
• "I acknowledge the traditional owners of the land on which we live, work and dream"
plus their flags as attached

```html
<!DOCTYPE html>
<html lang="en">
<head>
<meta charset="utf-8">
<title>Email Signature – Darina Qubrosi</title>
<link rel="stylesheet" href="https://fonts.googleapis.com/css2?family=Montserrat:wght@400;500;600;700;800&display=swap">
<style>
  :root {
    --orange: #f7941d;
    --navy: #2b2f3d;
    --white: #ffffff;
    --paper: #ececec;
    --strip: #d9d9d9;
    --photo-a: #7a6a5e;
    --photo-b: #c9b8a8;
  }
  * { box-sizing: border-box; margin: 0; padding: 0; }
  html, body {
    width: 822px; height: 1200px; overflow: hidden;
    background: var(--paper);
    font-family: "Montserrat", Arial, sans-serif;
  }
  .signature {
    position: absolute; left: 31px; top: 470px;
    width: 760px; height: 260px;
    background: var(--white);
    box-shadow: 0 2px 8px rgba(0,0,0,.12);
  }
  .signature__band {
    position: absolute; left: 0; top: 0; width: 100%; height: 128px;
    background: var(--orange);
  }
  .signature__strip {
    position: absolute; left: 0; bottom: 0; width: 100%; height: 14px;
    background: var(--strip);
  }
  .photo {
    position: absolute; left: 44px; top: 28px;
    width: 144px; height: 144px; border-radius: 50%;
    border: 6px solid var(--white);
    background: radial-gradient(circle at 50% 40%, var(--photo-b), var(--photo-a));
  }
  .brand {
    position: absolute; left: 40px; top: 186px; width: 152px;
    display: flex; align-items: center; justify-content: center; gap: 7px;
  }
  .brand__dot { width: 16px; height: 16px; border-radius: 50%; background: var(--orange); flex: none; }
  .brand__name {
    color: var(--orange); font-weight: 800; font-size: 13px;
    letter-spacing: .5px; text-transform: uppercase; white-space: nowrap;
  }
  .identity { position: absolute; left: 226px; top: 40px; }
  .identity__name {
    font-size: 27px; font-weight: 600; color: var(--navy);
    text-transform: uppercase; letter-spacing: .5px;
  }
  .identity__role { margin-top: 4px; font-size: 13px; color: var(--white); font-weight: 500; }
  .contacts {
    position: absolute; left: 520px; top: 14px; list-style: none;
  }
  .contacts li {
    display: flex; align-items: center; gap: 7px;
    font-size: 9.5px; color: var(--white); line-height: 1.2;
    margin-bottom: 5px; min-height: 16px;
  }
  .contacts .icon {
    width: 16px; height: 16px; border-radius: 50%; background: var(--white);
    flex: none; display: flex; align-items: center; justify-content: center;
  }
  .contacts .icon svg { width: 10px; height: 10px; }
  .divider {
    position: absolute; left: 222px; top: 150px; width: 3px; height: 74px;
    background: var(--orange);
  }
  .tagline {
    position: absolute; left: 244px; top: 163px; width: 360px;
    font-size: 17px; font-weight: 800; color: var(--navy);
    line-height: 1.35; text-transform: uppercase; letter-spacing: .2px;
    white-space: nowrap;
  }
  .social {
    position: absolute; right: 40px; top: 176px; display: flex; gap: 8px;
  }
  .social span { width: 22px; height: 22px; border-radius: 50%; background: var(--orange); }
</style>
</head>
<body>
  <section class="signature">
    <div class="signature__band"></div>
    <div class="signature__strip"></div>

    <div class="photo" role="img" aria-label="Portrait photograph of Darina Qubrosi"></div>

    <div class="brand">
      <span class="brand__dot"></span>
      <span class="brand__name">Mivrotel Haven</span>
    </div>

    <div class="identity">
      <h1 class="identity__name">Darina Qubrosi</h1>
      <p class="identity__role">Support Coordinator</p>
    </div>

    <ul class="contacts">
      <li><span class="icon"><svg viewBox="0 0 10 10"><path d="M5 0.5a3.2 3.2 0 0 0-3.2 3.2C1.8 6.2 5 9.5 5 9.5s3.2-3.3 3.2-5.8A3.2 3.2 0 0 0 5 .5zm0 4.5a1.3 1.3 0 1 1 0-2.6 1.3 1.3 0 0 1 0 2.6z" fill="#f7941d"/></svg></span>Unit 4, 517 Wattlebrook Lane,<br>Kemberly NSW 2893</li>
      <li><span class="icon"><svg viewBox="0 0 10 10"><path d="M2.3.8l1.4 1.9-.8 1.1c.6 1.2 1.5 2.1 2.7 2.7l1.1-.8 1.9 1.4-.7 1.6C4.5 8.5 1.5 5.5 1.3 1.5z" fill="#f7941d"/></svg></span>02 84427193</li>
      <li><span class="icon"><svg viewBox="0 0 10 10"><rect x="3" y=".8" width="4" height="8.4" rx=".8" fill="#f7941d"/><rect x="3.7" y="1.8" width="2.6" height="5.4" fill="#fff"/></svg></span>0427596314</li>
      <li><span class="icon"><svg viewBox="0 0 10 10"><rect x="1" y="2.3" width="8" height="5.4" fill="#f7941d"/><path d="M1 2.5l4 3 4-3" stroke="#fff" stroke-width=".8" fill="none"/></svg></span>darina.qu@mivrotelhaven.com</li>
      <li><span class="icon"><svg viewBox="0 0 10 10"><circle cx="5" cy="5" r="4" fill="none" stroke="#f7941d" stroke-width="1"/><ellipse cx="5" cy="5" rx="1.7" ry="4" fill="none" stroke="#f7941d" stroke-width=".8"/><path d="M1 5h8" stroke="#f7941d" stroke-width=".8"/></svg></span>www.mivrotelhaven.com</li>
    </ul>

    <div class="divider"></div>
    <p class="tagline">Specialist Provider of<br>Multicultural Support Services</p>

    <div class="social" aria-label="Social media links">
      <span></span><span></span><span></span>
    </div>
  </section>
</body>
</html>
```